Ferrant Valley Zoning Council Business Cards

We're looking for a business card design, simple as that. We're a local government agency that mainly performs building code enforcement, transportation planning, floodplain management, and GIS for Tobelle Parish in Louisiana, and other surround parishes. So you're not having to Google anything, GIS is, at it's core, mapping. Building Code Enforcement is just that, nothing more. Floodplain Management is to make sure the public is within what the government

Contact Information for Business Card

Our Address is

517 Marwick Street
Alexandria, LA 71489

Our phone is 3185529137
Our fax is 3185529142
Our website is www.fvzc.info
My email is dana@fvzc.info

Font styles to use
Serif
Sans Serif

Colors

Designer to choose colors to be used in the design.

Requirements
Must have
• I'm attaching our logo(several versions) that must be incorporated. The design should fit well with our existing logo. I can send photoshop files for our logo if needed. If possible, I'd like to be able to add names/info to each card for all of our employees once this is done.
Nice to have
• The Louisiana state seal is a bonus, and isn't specifically required.

```html
<!DOCTYPE html>
<html lang="en">
<head>
<meta charset="utf-8">
<title>Ferrant Valley Zoning Council – Business Card</title>
<link href="https://fonts.googleapis.com/css2?family=Montserrat:wght@700;800&family=Open+Sans:wght@400;600;700&display=swap" rel="stylesheet">
<style>
  :root {
    --page: #d9d9db;
    --card-white: #f4f4f4;
    --ink: #141414;
    --ink-soft: #3a3a3a;
    --rule: #cfcfcf;
    --green: #14ad1c;
    --lime: #d8f000;
    --yellow: #f2ee00;
    --orange: #f4a41c;
    --blue: #1463ff;
  }
  * { box-sizing: border-box; margin: 0; padding: 0; }
  html, body { width: 1200px; height: 1015px; overflow: hidden; background: var(--page); }
  .canvas {
    width: 1200px; height: 1015px;
    display: flex; flex-direction: column; align-items: center; justify-content: center; gap: 44px;
  }
  .card {
    width: 760px; height: 434px; position: relative; overflow: hidden;
    box-shadow: 0 6px 18px rgba(0,0,0,.18);
  }
  /* Back side */
  .card-back {
    background: linear-gradient(to bottom,
      var(--green) 0%, var(--lime) 32%, var(--yellow) 42%,
      var(--orange) 66%, #c9a27a 80%, var(--blue) 92%, var(--blue) 100%);
  }
  .card-back .back-name {
    position: absolute; left: 64%; top: 40%;
    font-family: "Montserrat", sans-serif; font-weight: 800;
    font-size: 30px; letter-spacing: 2px; color: var(--ink);
  }
  /* Front side */
  .card-front { background: var(--card-white); display: flex; }
  .brand {
    width: 52%; display: flex; align-items: center; justify-content: center; gap: 14px;
    padding-top: 70px;
  }
  .brand-dot { width: 52px; height: 52px; border-radius: 50%; background: var(--green); }
  .brand-name {
    font-family: "Montserrat", sans-serif; font-weight: 800;
    font-size: 84px; letter-spacing: 3px; color: var(--ink); line-height: 1;
  }
  .divider { width: 1px; background: linear-gradient(to bottom, transparent, var(--rule) 20%, var(--rule) 80%, transparent); margin: 56px 0; }
  .details {
    flex: 1; padding: 78px 0 0 44px;
    font-family: "Open Sans", sans-serif; color: var(--ink-soft); font-size: 19px; line-height: 1.35;
  }
  .person { font-weight: 700; font-size: 21px; color: var(--ink); text-transform: uppercase; letter-spacing: .3px; }
  .role { margin-bottom: 8px; }
  .contact-list { list-style: none; }
  .contact-list li { display: flex; align-items: center; gap: 8px; }
  .contact-list svg { width: 15px; height: 15px; fill: var(--ink); flex: none; }
  .address { margin-top: 6px; }
</style>
</head>
<body>
<main class="canvas">
  <section class="card card-back" role="img" aria-label="Back of card: green to yellow, orange and blue gradient with the council name">
    <span class="back-name">FVZC</span>
  </section>

  <section class="card card-front">
    <div class="brand">
      <span class="brand-dot"></span>
      <span class="brand-name">FVZC</span>
    </div>
    <div class="divider"></div>
    <div class="details">
      <p class="person">Marcus Delaune</p>
      <p class="role">Managing Director</p>
      <ul class="contact-list">
        <li><svg viewBox="0 0 16 16"><path d="M3 1h3l1.5 4-2 1.2a9 9 0 0 0 4.3 4.3L11 8.5l4 1.5v3a2 2 0 0 1-2 2A12 12 0 0 1 1 3a2 2 0 0 1 2-2z"/></svg>3185529137</li>
        <li><svg viewBox="0 0 16 16"><path d="M4 1h8v4H4zM1 6h14v7h-3v2H4v-2H1zm4 5v3h6v-3z"/></svg>3185529142</li>
        <li><svg viewBox="0 0 16 16"><path d="M1 3h14v10H1zm1.5 1.2V5l5.5 4 5.5-4v-.8L8 8z"/></svg>dana@fvzc.info</li>
        <li><svg viewBox="0 0 16 16"><circle cx="8" cy="8" r="7"/></svg>www.fvzc.info</li>
      </ul>
      <p class="address">517 Marwick Street<br>Alexandria, LA 71489</p>
    </div>
  </section>
</main>
</body>
</html>
```